Business Management Fortress

Assist with enhancing a powerpoint slide by providing a few design options for consideration. I have a template but open to any creative ideas.

Target Market(s)

Internal employees and stakeholders

Industry/Entity Type

Business Management, Finance, Accounting

Requirements
Must have
• Maintain a fortress, temple, or pyramid schema
Nice to have
• Scenic Background

```html
<!DOCTYPE html>
<html lang="en">
<head>
<meta charset="utf-8">
<title>Business Management Fortress</title>
<link rel="stylesheet" href="https://fonts.googleapis.com/css2?family=Bebas+Neue&family=Oswald:wght@500;600&display=swap">
<style>
  :root {
    --bg-light: #4f97d0;
    --bg-mid: #1f63b0;
    --bg-dark: #0b3a86;
    --roof-frame: #7f7f7f;
    --roof-panel: #dedede;
    --beam: #a6a6a6;
    --base-dark: #7f7f7f;
    --ink: #111111;
    --white: #ffffff;
    --people: #ffc000; --people-dark: #bf9000; --people-light: #ffe699;
    --innovation: #ed7d31; --innovation-dark: #c55a11; --innovation-light: #f8cbad;
    --intel: #70ad47; --intel-dark: #548235; --intel-light: #c5e0b4;
    --alliance: #5b9bd5; --alliance-dark: #2e75b6; --alliance-light: #bdd7ee;
  }
  html, body { margin: 0; padding: 0; overflow: hidden; background: var(--bg-dark); }
  .slide {
    position: relative; width: 1200px; height: 675px; overflow: hidden;
  }
  .scenic-backdrop {
    position: absolute; inset: 0;
    background:
      radial-gradient(ellipse at 20% 20%, rgba(255,255,255,0.18), transparent 55%),
      linear-gradient(135deg, var(--bg-light) 0%, var(--bg-mid) 55%, var(--bg-dark) 100%);
  }
  .fortress { position: absolute; inset: 0; width: 1200px; height: 675px; }
  .roof-label, .base-title, .base-items {
    font-family: "Oswald", "Bebas Neue", sans-serif; fill: var(--ink); text-anchor: middle;
  }
  .roof-label { font-size: 29px; font-weight: 600; letter-spacing: 3px; }
  .base-title { font-size: 21px; font-weight: 600; letter-spacing: 5px; }
  .base-items { font-size: 14.5px; font-weight: 600; }
  .pillar-label {
    font-family: "Bebas Neue", "Oswald", sans-serif; fill: var(--white); text-anchor: middle;
    font-size: 31px; filter: drop-shadow(1px 2px 1px rgba(0,0,0,0.45));
  }
  .pillar-icon { fill: rgba(255,255,255,0.88); }
</style>
</head>
<body>
<div class="slide">
  <div class="scenic-backdrop" role="img" aria-label="Blurred blue-toned office scene with a person working at a desk"></div>

  <svg class="fortress" viewBox="0 0 1280 720" aria-label="Business management fortress">
    <defs>
      <filter id="soft-shadow" x="-10%" y="-10%" width="120%" height="130%">
        <feDropShadow dx="0" dy="3" stdDeviation="4" flood-opacity="0.35"/>
      </filter>
    </defs>

    <!-- Roof -->
    <g class="roof" filter="url(#soft-shadow)">
      <polygon points="205,230 635,58 1072,232" fill="var(--roof-frame)"/>
      <polygon points="448,140 635,68 828,140 635,216" fill="var(--roof-panel)"/>
      <polygon points="245,222 432,150 615,222" fill="var(--roof-panel)"/>
      <polygon points="655,222 838,150 1024,222" fill="var(--roof-panel)"/>
      <text class="roof-label" x="622" y="138">PARTNER</text>
      <text class="roof-label" x="427" y="205">LEADER</text>
      <text class="roof-label" x="838" y="205">PROFIT</text>
    </g>

    <!-- Beam -->
    <rect x="192" y="228" width="878" height="40" rx="20" fill="var(--beam)" filter="url(#soft-shadow)"/>

    <!-- Pillars -->
    <g class="pillar pillar-people">
      <rect x="244" y="268" width="110" height="10" fill="var(--people-dark)"/>
      <rect x="254" y="278" width="90" height="14" fill="var(--people)"/>
      <rect x="269" y="292" width="60" height="40" fill="var(--people-light)"/>
      <rect x="269" y="514" width="60" height="30" fill="var(--people-light)"/>
      <rect x="254" y="543" width="90" height="15" fill="var(--people)"/>
      <rect x="244" y="558" width="110" height="21" fill="var(--people-dark)"/>
      <rect x="211" y="332" width="176" height="182" rx="6" fill="var(--people)"/>
      <rect class="pillar-icon" x="268" y="356" width="62" height="58" rx="6" role="img" aria-label="Family icon"/>
      <text class="pillar-label" x="299" y="467">PEOPLE</text>
    </g>

    <g class="pillar pillar-innovation">
      <rect x="467" y="268" width="110" height="10" fill="var(--innovation-dark)"/>
      <rect x="477" y="278" width="90" height="14" fill="var(--innovation)"/>
      <rect x="492" y="292" width="60" height="40" fill="var(--innovation-light)"/>
      <rect x="492" y="514" width="60" height="30" fill="var(--innovation-light)"/>
      <rect x="477" y="543" width="90" height="15" fill="var(--innovation)"/>
      <rect x="467" y="558" width="110" height="21" fill="var(--innovation-dark)"/>
      <rect x="434" y="332" width="176" height="182" rx="6" fill="var(--innovation)"/>
      <rect class="pillar-icon" x="496" y="358" width="50" height="52" rx="6" role="img" aria-label="Puzzle pieces icon"/>
      <text class="pillar-label" x="527" y="467">INNOVATION</text>
    </g>

    <g class="pillar pillar-intelligence">
      <rect x="689" y="268" width="110" height="10" fill="var(--intel-dark)"/>
      <rect x="699" y="278" width="90" height="14" fill="var(--intel)"/>
      <rect x="714" y="292" width="60" height="40" fill="var(--intel-light)"/>
      <rect x="714" y="514" width="60" height="30" fill="var(--intel-light)"/>
      <rect x="699" y="543" width="90" height="15" fill="var(--intel)"/>
      <rect x="689" y="558" width="110" height="21" fill="var(--intel-dark)"/>
      <rect x="656" y="332" width="176" height="182" rx="6" fill="var(--intel)"/>
      <rect class="pillar-icon" x="718" y="354" width="50" height="58" rx="6" role="img" aria-label="Head with gears icon"/>
      <text class="pillar-label" x="741" y="456">BUSINESS</text>
      <text class="pillar-label" x="741" y="483">INTELLIGENCE</text>
    </g>

    <g class="pillar pillar-alliances">
      <rect x="912" y="268" width="110" height="10" fill="var(--alliance-dark)"/>
      <rect x="922" y="278" width="90" height="14" fill="var(--alliance)"/>
      <rect x="937" y="292" width="60" height="40" fill="var(--alliance-light)"/>
      <rect x="937" y="514" width="60" height="30" fill="var(--alliance-light)"/>
      <rect x="922" y="543" width="90" height="15" fill="var(--alliance)"/>
      <rect x="912" y="558" width="110" height="21" fill="var(--alliance-dark)"/>
      <rect x="879" y="332" width="176" height="182" rx="6" fill="var(--alliance)"/>
      <rect class="pillar-icon" x="944" y="358" width="48" height="52" rx="5" role="img" aria-label="Strategy playbook icon"/>
      <text class="pillar-label" x="968" y="456">STRATEGIC</text>
      <text class="pillar-label" x="968" y="483">ALLIANCES</text>
    </g>

    <!-- Foundation -->
    <g class="foundation" filter="url(#soft-shadow)">
      <rect x="180" y="579" width="888" height="38" rx="5" fill="var(--beam)"/>
      <rect x="162" y="615" width="918" height="43" rx="5" fill="var(--base-dark)"/>
      <text class="base-title" x="626" y="606">FIDUCIARY RESPONSIBILITIES</text>
      <text class="base-items" x="612" y="642">ACCURATE FINANCIALS / INTERNAL CONTROLS / BRAND PROTECTION / COMPLIANCE / ETHICS / COST MANAGEMENT</text>
    </g>
  </svg>
</div>
</body>
</html>
```